Create a wordpress website for Tavoro business solution

This project is to create a complete website with all pages.

Overview
The purpose of this project is to create a full complete website with all pages (16 pages). The site should be professional and modern. The site is for an IT recruiting and IT training company. The site needs to be easy to administer and update content. It should be simple to add pages, videos and testimonials later. I will leave the site layout, color schemes and flow to the designers.

Navigation Menu (Home, who we are, what we do, what makes us different, why it matters, candidate portal, contact us, Blog)

WHO WE ARE should be a drop down menu with link to pages (about us, mission, vision and purpose, our team)

WHAT WE DO should be drop down menu with link to the following pages (IT Recruiting, IT Training, Hardware and software sales)

What makes us different should be single page with different paragraph titles. (We live what we do, we don't compromise quality, we share knowledge, staffing guarantee)

Why it matters should be single page with paragraph titles. (Quickly fill positions, candidate career development)

Candidate portal should links to my portal login page. I can add the correct URL later. I just need it to link to somewhere. I can change it.

Contact us should have (address, phone number, google map and a form to submit request for a call back)

Blog - This link should launch a wordpress blogging module

Target Market(s)

IT RECRUITING AND CONSULTING

Industry/Entity Type

It Company

Coding

Coded - Design and coding required

Requirements
Must have
• Company Logo
• Navigation Menu (Home, who we are, what we do, what makes us different, why it matters, candidate portal, contact us)
• WHO WE ARE should be a drop down menu with link to pages (about us, mission, vision and purpose, our team)
• WHAT WE DO should be drop down menu with link to the following pages (IT Recruiting, IT Training, Hardware and software sales)
• What makes us different should be single page with different paragraph titles. (We live what we do, we don't compromise quality, we share knowledge, staffing guarantee)
• Why it matters should be single page with paragraph titles. (Quickly fill positions, candidate career development)
• Candidate portal should links to my portal login page. I can add the correct URL later. I just need it to link to somewhere. I can change it.
• Contact us should have (address, phone number, google map and a form to submit request for a call back)

```html
<!DOCTYPE html>
<html lang="en">
<head>
<meta charset="utf-8">
<title>Tavoro Business Solution</title>
<link href="https://fonts.googleapis.com/css2?family=Roboto:wght@400;500;700&family=Roboto+Condensed:wght@400;700&display=swap" rel="stylesheet">
<style>
:root{
  --brand:#0d4f9c;
  --ink:#222;
  --paper:#fbfbfa;
  --rule:#c9c9c9;
  --footer:#0c4e9d;
  --bar:#0a0a0a;
}
*{margin:0;padding:0;box-sizing:border-box}
html,body{width:771px;height:1200px;overflow:hidden;background:#fff}
body{font-family:"Roboto",Arial,sans-serif;color:var(--ink)}
.page{position:relative;width:771px;height:1200px;overflow:hidden;background:var(--paper)}
.abs{position:absolute}
.heading{font-family:"Roboto Condensed","Arial Narrow",sans-serif;font-weight:700;color:var(--brand);text-transform:uppercase;letter-spacing:.2px}
.copy{font-size:6.2px;line-height:12.8px;color:var(--ink)}

/* header */
.site-header{left:0;top:0;width:771px;height:22px;background:#fff}
.brand-name{left:160px;top:3px;font-size:13px;font-weight:500;color:var(--brand);letter-spacing:.2px;display:flex;align-items:center;gap:4px}
.brand-name .mark{width:6px;height:6px;background:var(--brand);display:inline-block}
.brand-name small{position:absolute;left:10px;top:14px;font-size:3.4px;letter-spacing:.6px;color:var(--brand);white-space:nowrap}
.main-nav{position:absolute;right:159px;top:8px;display:flex;gap:9px}
.main-nav a{font-size:5.8px;color:#222;text-decoration:none;white-space:nowrap;text-transform:uppercase}

/* hero */
.hero{left:0;top:22px;width:771px;height:230px;background:linear-gradient(100deg,#cfd3d8 0%,#bfc6cd 35%,#d8dadc 55%,#a9b0ba 75%,#4a4f5a 100%)}
.hero-portrait{left:244px;top:82px;width:84px;height:86px;border-radius:50%;background:radial-gradient(circle at 50% 40%,#e7d8cc,#6b6f7a 70%,#2a2d36);border:3px solid #fff;box-shadow:0 0 0 1px #aaa}
.hero-title{left:342px;top:88px;font-weight:500;font-size:14px;color:#fff;text-transform:uppercase;letter-spacing:.3px}
.hero-copy{left:342px;top:109px;width:200px;font-size:6.2px;line-height:11.2px;color:#fff}
.hero-link{left:342px;top:150px;font-size:5.6px;font-weight:700;color:#fff}
.slider-dot{left:605px;width:6px;height:6px;background:#fff;border:1px solid #ddd}
.slider-dot.active{background:var(--brand)}

/* about */
.about-title{left:0;width:771px;top:268px;text-align:center;font-size:14.5px}
.col-head{top:304px;font-size:11px}
.about-divider{left:386px;top:302px;width:1px;height:92px;background:var(--rule)}
.btn-outline{border:1px solid var(--brand);border-radius:9px;color:var(--brand);font-size:5.4px;font-weight:700;display:flex;align-items:center;justify-content:center;background:#fff}

/* team */
.team{left:0;top:445px;width:771px;height:195px;background:linear-gradient(90deg,#c9d7e1 0%,#b6c8d4 25%,#dfe4e8 50%,#c8ccd0 75%,#aeb5bd 100%)}
.team-veil{left:0;top:445px;width:771px;height:195px;background:rgba(255,255,255,.35)}
.team-title{left:0;width:771px;top:462px;text-align:center;font-size:14.5px}
.member-name{top:506px;font-size:11px;font-weight:500;font-family:"Roboto",sans-serif}
.member-photo{width:58px;height:58px;border-radius:50%;background:radial-gradient(circle at 50% 40%,#e5cdb8,#7b7f88 72%,#3d4049);border:2px solid #fff}
.member-copy{top:503px;width:140px;font-size:6.2px;line-height:11.2px}
.team-dot{top:615px;width:6px;height:6px;border-radius:50%;background:var(--brand)}
.team-dot.empty{background:transparent;border:1px solid var(--brand)}

/* candidate */
.candidate{left:0;top:640px;width:771px;height:187px;background:linear-gradient(90deg,#f1f3f5 0%,#e7ecf0 40%,#eceff2 70%,#f6f6f6 100%)}
.candidate-title{left:0;width:771px;top:657px;text-align:center;font-size:14.5px}
.diff-title{left:160px;top:689px;font-weight:500;font-size:17.5px;color:var(--brand);text-transform:uppercase}
.laptop{left:412px;top:688px;width:200px;height:116px;background:linear-gradient(160deg,#d9dadc 0%,#9a9ca2 40%,#c9cbce 100%)}

/* contact */
.contact-title{left:0;width:771px;top:842px;text-align:center;font-size:14.5px}
.field{left:160px;width:150px;border:1px solid var(--brand);background:#fff;font-size:5.6px;color:#333;padding:6px 7px;text-transform:uppercase}
.submit{left:206px;top:1030px;width:58px;height:20px;border:1px solid var(--brand);background:#fff;color:var(--brand);font-size:5.8px;font-weight:500;display:flex;align-items:center;justify-content:center}
.map{left:335px;top:874px;width:276px;height:180px;background:linear-gradient(135deg,#e8e4d8 0%,#dcd9cf 45%,#cfe0c4 70%,#e6e1cf 100%)}

/* footer */
.site-footer{left:0;top:1073px;width:771px;height:104px;background:var(--footer);color:#fff}
.foot-head{top:1091px;font-size:9px;font-weight:500;color:#fff;text-transform:uppercase}
.foot-head.plain{text-transform:none}
.foot-copy{font-size:5.8px;line-height:10px;color:#fff}
.foot-links a{display:block;font-size:5.2px;line-height:10px;color:#fff;text-decoration:none;text-transform:uppercase}
.social{top:1126px;width:11px;height:11px;background:#fff}
.to-top{left:672px;top:1104px}
.chat{left:633px;top:1162px;width:115px;height:14px;background:#fff;font-size:5.6px;color:#333;padding:4px 6px}
.chat-badge{left:662px;top:1155px;width:9px;height:9px;border-radius:50%;background:#c21c1c;color:#fff;font-size:5px;display:flex;align-items:center;justify-content:center}
.bottom-bar{left:0;top:1177px;width:771px;height:23px;background:var(--bar);color:#fff;font-size:5px;padding:8px 160px}
</style>
</head>
<body>
<div class="page">

  <header class="abs site-header">
    <div class="abs brand-name"><span class="mark"></span>tavoro<small>BUSINESS SOLUTION LLC</small></div>
    <nav class="main-nav">
      <a href="#">Home</a>
      <a href="#">Who We Are</a>
      <a href="#">What We Do</a>
      <a href="#">What Makes Us Different</a>
      <a href="#">Why It Matters</a>
      <a href="#">Candidate Portal</a>
      <a href="#">Contact Us</a>
      <a href="#">Blog</a>
    </nav>
  </header>

  <section>
    <div class="abs hero" role="img" aria-label="Business team meeting collage with a pointing hand"></div>
    <div class="abs hero-portrait" role="img" aria-label="Portrait of a businessman"></div>
    <h2 class="abs hero-title">Arlen Caption</h2>
    <p class="abs hero-copy">Lorem Ipsum has been the industry's standard dummy text ever since the 1500s, when an unknown printer took a galley of type and scrambled it to make a type specimen book.</p>
    <a class="abs hero-link">Read Now!</a>
    <span class="abs slider-dot" style="top:114px"></span>
    <span class="abs slider-dot active" style="top:127px"></span>
    <span class="abs slider-dot" style="top:140px"></span>
    <span class="abs slider-dot" style="top:153px"></span>
  </section>

  <section>
    <h2 class="abs heading about-title">About Us</h2>
    <h3 class="abs heading col-head" style="left:160px;width:213px;text-align:right">Simply Dummy</h3>
    <h3 class="abs heading col-head" style="left:396px">Only Five Centuries,</h3>
    <div class="abs about-divider"></div>
    <p class="abs copy" style="left:160px;top:334px;width:214px;text-align:justify;text-align-last:right">Lorem Ipsum is simply dummy text of the printing and typesetting industry. Lorem Ipsum has been the industry's standard dummy text ever since the 1500s, when an unknown printer took a galley of type and scrambled it to make a type specimen book.</p>
    <p class="abs copy" style="left:396px;top:334px;width:214px">Lorem Ipsum is simply dummy text of the printing and typesetting industry. Lorem Ipsum has been the industry's standard dummy text ever since the 1500s, when an unknown printer took a galley of type and scrambled it to make a type speci.men book.</p>
    <a class="abs btn-outline" style="left:357px;top:411px;width:58px;height:15px">Read More</a>
  </section>

  <section>
    <div class="abs team" role="img" aria-label="Blurred office background with a smiling man"></div>
    <div class="abs team-veil"></div>
    <h2 class="abs heading team-title">Our Team</h2>
    <h3 class="abs heading member-name" style="left:174px">Rowan</h3>
    <div class="abs member-photo" role="img" aria-label="Portrait of team member Rowan" style="left:161px;top:527px"></div>
    <p class="abs copy member-copy" style="left:230px">Lorem ipsum dolor sit amet, consectetur adipiscing elit, sed do eiusmod tempor incididunt ut labore et dolore magna aliqua. Ut enim ad minim veniam, quis nostrud exercitation ullamco laboris nisi ut aliquip ex ea commodo consequat. Duis aute irure dolor in reprehenderit in voluptate velit esse cillum dolore eu fugiat nulla pariatur.</p>
    <h3 class="abs heading member-name" style="left:418px">Delia</h3>
    <div class="abs member-photo" role="img" aria-label="Portrait of team member Delia" style="left:405px;top:527px"></div>
    <p class="abs copy member-copy" style="left:475px">Lorem ipsum dolor sit amet, consectetur adipiscing elit, sed do eiusmod tempor incididunt ut labore et dolore magna aliqua. Ut enim ad minim veniam, quis nostrud exercitation ullamco laboris nisi ut aliquip ex ea commodo consequat. Duis aute irure dolor in reprehenderit in voluptate velit esse cillum dolore eu fugiat nulla pariatur.</p>
    <span class="abs team-dot" style="left:370px"></span>
    <span class="abs team-dot empty" style="left:383px"></span>
    <span class="abs team-dot" style="left:395px"></span>
  </section>

  <section>
    <div class="abs candidate" role="img" aria-label="Faded office scene with a woman at work"></div>
    <h2 class="abs heading candidate-title">Candidate Portal</h2>
    <h3 class="abs diff-title">What Makes Us Different</h3>
    <p class="abs copy" style="left:160px;top:725px;width:230px;line-height:11.2px">Lorem Ipsum has been the industry's standard dummy text ever since the 1500s, when an unknown printer took a galley of type and scrambled it to make a type specimen book. It has survived not only five centuries, but also the leap into electronic typesetting, remaining essentially unchanged</p>
    <a class="abs btn-outline" style="left:160px;top:793px;width:58px;height:15px">Read More</a>
    <div class="abs laptop" role="img" aria-label="Laptop computer"></div>
  </section>

  <section>
    <h2 class="abs heading contact-title">Contact Us</h2>
    <div class="abs field" style="top:875px;height:19px">Name :</div>
    <div class="abs field" style="top:898px;height:20px">Email :</div>
    <div class="abs field" style="top:922px;height:20px">Phone :</div>
    <div class="abs field" style="top:946px;height:78px">Meassage</div>
    <div class="abs submit">SUMBIT</div>
    <div class="abs map" role="img" aria-label="Street map of the office location"></div>
  </section>

  <footer>
    <div class="abs site-footer"></div>
    <h4 class="abs foot-head" style="left:160px">Selma</h4>
    <p class="abs foot-copy" style="left:160px;top:1106px;width:110px">Lorem Ipsum is simply dummy text printing and typesetting industry.</p>
    <p class="abs foot-copy" style="left:160px;top:1134px;width:110px">Lorem Ipsum is simply dummy text of the printing and typesetting</p>
    <h4 class="abs foot-head" style="left:295px">Overview</h4>
    <div class="abs foot-links" style="left:295px;top:1109px">
      <a href="#">Home</a><a href="#">About Us</a><a href="#">Our Team</a><a href="#">Blog</a><a href="#">Contact Us</a>
    </div>
    <h4 class="abs foot-head plain" style="left:373px">Harbor City, NY</h4>
    <p class="abs foot-copy" style="left:373px;top:1106px;width:125px">Lorem Ipsum is simply dummy text of the printing and typesetting industry.</p>
    <h4 class="abs foot-head plain" style="left:373px;top:1129px">Phone</h4>
    <p class="abs foot-copy" style="left:373px;top:1142px">000 000 000</p>
    <h4 class="abs foot-head plain" style="left:528px">E-mail</h4>
    <p class="abs foot-copy" style="left:528px;top:1108px">info.tavoro.business.solution</p>
    <span class="abs social" style="left:529px"></span>
    <span class="abs social" style="left:543px"></span>
    <span class="abs social" style="left:558px"></span>
    <span class="abs social" style="left:573px"></span>
    <svg class="abs to-top" width="22" height="14" viewBox="0 0 22 14"><polyline points="2,12 11,3 20,12" fill="none" stroke="#fff" stroke-width="3"/></svg>
    <div class="abs chat">Message
      <svg style="position:absolute;right:6px;top:3px" width="8" height="8" viewBox="0 0 8 8"><circle cx="4" cy="4" r="3.4" fill="none" stroke="#333" stroke-width=".7"/><polyline points="2.4,4.8 4,3.2 5.6,4.8" fill="none" stroke="#333" stroke-width=".7"/></svg>
    </div>
    <span class="abs chat-badge">1</span>
    <div class="abs bottom-bar">© 2016-17 Tavoro Business Solution All rights reserved</div>
  </footer>

</div>
</body>
</html>
```